Professional services business card

This is for a new business in New Zealand, providing professional advice to boards of directors of companies
The point of difference is a strong blend of Financial and IT knowledge

Target audience are senior business executives, CEO/CFO/President, etc.
So, simple but appealing
Business colours are orange and blue

Sample logo attached
proposed Content also attached - feedback on wording is welcome
Updates

Please provide for a logo to be added - about 30 mm wide and 10 mm high

the company name is "Korvale Meridian Ltd" - logo now uploaded to the project brief

Information to include are now in the second file that was uploaded

Industry/Entity Type

Business

```html
<!DOCTYPE html>
<html lang="en">
<head>
<meta charset="utf-8">
<title>Korvale Meridian Ltd – Business Card</title>
<link href="https://fonts.googleapis.com/css2?family=Open+Sans:wght@400;600;700&display=swap" rel="stylesheet">
<style>
  :root {
    --bg: #a9aaac;
    --blue: #0892cf;
    --orange: #f0923a;
    --white: #ffffff;
    --ink-soft: #e6f4fb;
  }
  * { box-sizing: border-box; margin: 0; padding: 0; }
  html, body { width: 1200px; height: 1000px; overflow: hidden; }
  body {
    background: var(--bg);
    font-family: "Open Sans", Arial, sans-serif;
    position: relative;
  }
  .card {
    position: absolute;
    width: 620px;
    height: 350px;
    border-radius: 34px;
    overflow: hidden;
    background: var(--blue);
    box-shadow: 0 18px 30px rgba(0,0,0,0.18);
  }
  .card--front { left: 140px; top: 120px; }
  .card--back  { left: 500px; top: 530px; }

  .card__head {
    height: 148px;
    background: var(--white);
    border-bottom: 6px solid var(--orange);
    display: flex;
    align-items: center;
    justify-content: center;
  }
  .brand {
    display: flex;
    align-items: center;
    gap: 12px;
    color: var(--blue);
    font-weight: 700;
    font-size: 40px;
    letter-spacing: -0.5px;
  }
  .brand__dot {
    width: 18px; height: 18px;
    border-radius: 50%;
    background: var(--orange);
  }

  /* front */
  .holder {
    position: absolute;
    left: 34px;
    top: 258px;
    color: var(--white);
  }
  .holder__name {
    font-weight: 700;
    font-size: 19px;
    letter-spacing: 3px;
  }
  .holder__credentials {
    font-size: 11.5px;
    letter-spacing: 0.5px;
  }
  .contact {
    position: absolute;
    left: 252px;
    top: 184px;
    color: var(--white);
    font-size: 13.5px;
    letter-spacing: 0.4px;
    line-height: 1.45;
  }
  .contact__company { font-weight: 700; font-size: 16px; }
  .contact__row { display: flex; align-items: center; gap: 8px; margin-top: 2px; }
  .contact__row svg { flex: none; }

  /* back */
  .services {
    list-style: none;
    position: absolute;
    left: 42px;
    top: 180px;
    color: var(--white);
    font-size: 19px;
    letter-spacing: 0.4px;
  }
  .services li { display: flex; align-items: center; gap: 10px; height: 31px; }
</style>
</head>
<body>

<section class="card card--front">
  <header class="card__head">
    <div class="brand"><span class="brand__dot"></span>Korvale Meridian</div>
  </header>
  <div class="holder">
    <p class="holder__name">TAMSIN REYES</p>
    <p class="holder__credentials">M.Com,ACA(NZ),ACMA</p>
  </div>
  <div class="contact">
    <p class="contact__company">Korvale Meridian Ltd</p>
    <p>PO Box 40217, Harbour Quay, Wellington, 6011</p>
    <p class="contact__row">
      <svg width="16" height="14" viewBox="0 0 16 14"><rect width="16" height="14" rx="2" fill="#fff"/><path d="M4 3c1 3 3 6 7 8l1.5-1.5-2-1.5-1 1c-1.5-.8-2.8-2.2-3.5-3.5l1-1-1.5-2z" fill="#0892cf"/></svg>
      021 555 0148
    </p>
    <p class="contact__row">
      <svg width="16" height="12" viewBox="0 0 16 12"><rect x="0.75" y="0.75" width="14.5" height="10.5" fill="none" stroke="#fff" stroke-width="1.5"/><path d="M1 1l7 6 7-6" fill="none" stroke="#fff" stroke-width="1.5"/></svg>
      T.Reyes@korvalemeridian.com
    </p>
    <p class="contact__row">
      <svg width="16" height="14" viewBox="0 0 16 14"><rect width="16" height="14" rx="2" fill="#fff"/></svg>
      http://www.korvalemeridian.com/tamsin
    </p>
  </div>
</section>

<section class="card card--back">
  <header class="card__head">
    <div class="brand"><span class="brand__dot"></span>Korvale Meridian</div>
  </header>
  <ul class="services">
    <li><svg width="24" height="20" viewBox="0 0 24 20"><path d="M2 11l6 6L22 2" fill="none" stroke="#fff" stroke-width="3" stroke-linecap="round" stroke-linejoin="round"/></svg>Governance</li>
    <li><svg width="24" height="20" viewBox="0 0 24 20"><path d="M2 11l6 6L22 2" fill="none" stroke="#fff" stroke-width="3" stroke-linecap="round" stroke-linejoin="round"/></svg>Good Stewardship</li>
    <li><svg width="24" height="20" viewBox="0 0 24 20"><path d="M2 11l6 6L22 2" fill="none" stroke="#fff" stroke-width="3" stroke-linecap="round" stroke-linejoin="round"/></svg>Financial Insight</li>
    <li><svg width="24" height="20" viewBox="0 0 24 20"><path d="M2 11l6 6L22 2" fill="none" stroke="#fff" stroke-width="3" stroke-linecap="round" stroke-linejoin="round"/></svg>Information Technology Insight</li>
    <li><svg width="24" height="20" viewBox="0 0 24 20"><path d="M2 11l6 6L22 2" fill="none" stroke="#fff" stroke-width="3" stroke-linecap="round" stroke-linejoin="round"/></svg>Mentoring and Business Advice</li>
  </ul>
</section>

</body>
</html>
```